Elegant wordpress web page for wedding rental of hand sanitizers

We want to rent our hand sanitizing towers out for high-end weddings. We need a very elegant, sophisticated page that describes our offering. You can see an ugly first draft here: purvant.com/weddings
Target Market(s)
Wedding planners, wedding parents
Number of Pages Required
1 page
Font styles to use
Serif
Script
Colors
Designer to choose colors to be used in the design.
Requirements
Nice to have
- Two wedding-related sites for inspiration: lacetrellisweddings-dot-com and fennoreventservices-dot-com

```html
<!DOCTYPE html>
<html lang="en">
<head>
<meta charset="utf-8">
<title>Purvant – Wedding Hand Sanitizer Rental</title>
<link href="https://fonts.googleapis.com/css2?family=Playball&family=Poppins:wght@300;400;500;600&display=swap" rel="stylesheet">
<style>
:root{
  --blue:#1c93d6;
  --blue-deep:#0c78c9;
  --blue-light:#2bb0d6;
  --ink:#222a33;
  --muted:#5c636b;
  --dark:#131a2a;
  --white:#ffffff;
  --pale:#eaf5fb;
}
*{margin:0;padding:0;box-sizing:border-box}
html,body{width:1200px;height:4570px;overflow:hidden;background:var(--white)}
body{position:relative;font-family:'Poppins',sans-serif;color:var(--ink)}
.abs{position:absolute}
.script{font-family:'Playball',cursive;font-weight:400}

/* header */
.site-header{left:0;top:0;width:1200px;height:82px;background:var(--white);z-index:5}
.brand{left:150px;top:18px;font-size:38px;font-weight:600;color:var(--blue);letter-spacing:-1px;line-height:1}
.main-nav{font-size:12.5px;font-weight:500;color:var(--ink)}
.main-nav a{position:absolute;white-space:nowrap;text-decoration:none;color:inherit}
.main-nav .active{color:var(--blue)}
.quote-btn{left:896px;top:0;width:153px;height:100px;background:var(--blue);color:var(--white);font-size:16px;font-weight:500;text-align:center;padding-top:30px;z-index:6}

/* hero */
.hero-bg{left:0;top:82px}
.hero-kicker{left:150px;top:205px;font-size:25px;font-weight:300;color:var(--white)}
.hero-title{left:150px;top:244px;font-size:56px;line-height:58px;color:var(--white)}
.btn{display:flex;align-items:center;justify-content:center;border-radius:24px;font-weight:600;font-size:14px;white-space:nowrap}
.btn-solid{left:151px;top:399px;width:147px;height:43px;background:var(--blue);color:var(--white)}
.btn-ghost{left:320px;top:399px;width:149px;height:43px;border:2px solid var(--white);color:var(--white)}
.slide-arrow{width:38px;height:38px;border-radius:50%;background:rgba(0,0,0,.55);color:var(--white);display:flex;align-items:center;justify-content:center;font-size:18px}
.dots{left:557px;top:548px;display:flex;gap:9px}
.dots span{width:13px;height:13px;border-radius:50%;border:2px solid var(--white)}
.dots .on{background:var(--blue);border-color:var(--blue)}
.placeholder{background:linear-gradient(180deg,#e3dcd8,#f1f1f1 55%,#e6e6e6)}
.hero-photo{left:900px;top:170px;width:150px;height:410px;border-radius:10px}

/* headings */
.sec-title{font-size:46px;color:var(--ink);white-space:nowrap}
.center{text-align:center;left:0;width:1200px}
.lead{font-size:14px;line-height:23px;color:var(--muted)}

/* unique */
.products-photo{left:335px;top:852px;width:520px;height:470px;border-radius:16px;background:linear-gradient(180deg,#efe9e6,#f6f6f6 60%,#efefef)}
.feature{display:flex;align-items:center;gap:14px;font-size:17px;font-weight:500;color:var(--ink);white-space:nowrap}
.drop{width:46px;height:56px;flex:none}
.pill{background:var(--white);color:var(--blue);box-shadow:0 4px 18px rgba(28,147,214,.22);border-radius:26px;font-size:14px;font-weight:500}

/* customize band */
.band-bg{left:0;top:1570px}
.frame-line{left:112px;top:1700px;width:410px;height:342px;border:4px solid var(--white);border-right:none;border-bottom:none;border-radius:110px 0 0 0}
.band-photo{left:151px;top:1736px;width:405px;height:341px;border-radius:110px 0 110px 0;background:linear-gradient(135deg,#6e4a3a,#b08a74 45%,#d8cfc8 70%,#7d5f4e)}
.band-title{left:621px;top:1705px;font-size:44px;color:var(--white);white-space:nowrap}
.band-sub{left:621px;top:1770px;font-size:15px;color:var(--white)}
.band-item{left:615px;display:flex;align-items:center;gap:20px;font-size:15px;line-height:27px;color:var(--white);width:440px}

/* greet */
.greet-title{left:151px;top:2290px;font-size:44px;line-height:52px;color:var(--ink)}
.care-item{left:151px;display:flex;align-items:center;gap:22px;font-size:15px;line-height:26px;color:var(--muted);width:480px}
.greet-photo{left:760px;top:2237px;width:300px;height:603px;border-radius:12px;background:linear-gradient(180deg,#d3d8cc 0%,#ebe8e4 50%,#f2f2f2 100%)}

/* review */
.review-bg{left:0;top:2840px;width:1200px;height:515px;background:linear-gradient(90deg,#3a2617 0%,#7c5532 30%,#3b2817 50%,#6b4a2b 75%,#2f2013 100%)}
.review-photo{left:70px;top:2905px;width:185px;height:450px;border-radius:10px}
.review-kicker{left:508px;top:2928px;font-size:15px;font-weight:500;color:var(--white)}
.review-title{left:508px;top:2962px;font-size:44px;line-height:56px;color:var(--white)}
.round-arrow{width:32px;height:32px;border-radius:50%;border:1.5px solid var(--white);color:var(--white);display:flex;align-items:center;justify-content:center;font-size:16px}
.review-card{left:506px;top:3097px;width:545px;height:347px;border-radius:60px 0 90px 0;background:linear-gradient(160deg,var(--blue-deep),var(--blue-light))}
.quote{left:540px;top:3138px;width:477px;text-align:center;font-size:14.5px;line-height:30px;color:var(--white)}
.avatar{border-radius:50%;background:linear-gradient(160deg,#d7c3b4,#8a6b5a)}
.reviewer{left:717px;top:3338px;font-size:18px;font-weight:500;color:var(--white)}
.reviewer-role{left:720px;top:3376px;font-size:14px;color:var(--white)}

/* offers */
.offer-kicker{left:151px;top:3538px;font-size:15px;font-weight:500;color:var(--blue)}
.offers-title{left:151px;top:3566px;font-size:44px;color:var(--ink)}
.offer-card{left:153px;top:3804px;width:433px;height:128px;border-radius:64px;background:var(--white);box-shadow:0 4px 24px rgba(0,0,0,.1)}
.offer-price{left:286px;font-size:12.5px;color:var(--muted)}
.offer-price b{color:var(--blue);font-weight:500}
.offer-name{left:286px;font-size:20px;font-weight:500;color:var(--ink)}
.offer-desc{left:286px;font-size:13px;line-height:21px;color:var(--muted);width:300px}
.collage{box-shadow:0 4px 18px rgba(0,0,0,.15)}

/* footer */
.footer-bg{left:0;top:4160px}
.footer-brand{left:0;width:1200px;text-align:center;top:4245px;font-size:44px;font-weight:600;color:var(--blue);letter-spacing:-1px}
.foot-head{top:4347px;font-size:17px;font-weight:500;color:var(--white)}
.foot-line{left:160px;display:flex;align-items:center;gap:14px;font-size:15px;color:var(--white)}
.social{width:40px;height:40px;border-radius:50%;border:1.5px solid var(--white)}
.email{left:779px;top:4393px;width:259px;height:33px;border:1px solid #9aa0ab;background:var(--white);font-size:12px;color:#444;padding:9px 12px}
.subscribe{left:779px;top:4437px;width:109px;height:34px;border-radius:18px;background:var(--blue);color:var(--white);font-size:12px;font-weight:600}
.copy{left:0;width:1200px;text-align:center;top:4532px;font-size:13.5px;color:#c9ccd3}
.rule{left:0;top:4508px;width:1200px;height:1px;background:#2a3244}
</style>
</head>
<body>

<header class="abs site-header">
  <div class="abs brand">purvant</div>
  <nav class="abs main-nav" style="left:0;top:44px">
    <a class="active" style="left:400px">HOME</a>
    <a style="left:465px">ABOUT</a>
    <a style="left:536px">PRODUCTS</a>
    <a style="left:632px">INDUSTRY SOLUTIONS</a>
    <a style="left:799px">CONTACT</a>
  </nav>
</header>
<div class="abs quote-btn">GET A QUOTE</div>

<!-- hero -->
<svg class="abs hero-bg" width="1200" height="580" viewBox="0 82 1200 580" role="img" aria-label="Wedding ceremony arch with draped fabric, flowers and candles in front of a stone wall">
  <defs>
    <linearGradient id="heroTone" x1="0" y1="0" x2="1" y2="1">
      <stop offset="0" stop-color="#4a4640"/>
      <stop offset=".45" stop-color="#8b7d6c"/>
      <stop offset=".8" stop-color="#6a6056"/>
      <stop offset="1" stop-color="#cfc8be"/>
    </linearGradient>
    <linearGradient id="swoosh" x1="0" y1="0" x2="1" y2="0">
      <stop offset="0" stop-color="#0a5fb8"/>
      <stop offset=".5" stop-color="#1c93d6"/>
      <stop offset="1" stop-color="#2bb0d6"/>
    </linearGradient>
  </defs>
  <path d="M0 82H1200V505Q600 640 0 505Z" fill="url(#heroTone)"/>
  <path d="M150 565Q600 700 1050 565Q600 662 150 565Z" fill="url(#swoosh)"/>
</svg>
<div class="abs hero-photo placeholder" role="img" aria-label="Photo of a custom sanitizer stand with a couple's wedding portrait"></div>
<div class="abs hero-kicker">Customize Your Sanitizer With</div>
<div class="abs hero-title script">Any Photo, Any Size &amp;<br>Any Shape</div>
<div class="abs btn btn-solid">RENT NOW</div>
<div class="abs btn btn-ghost">READ MORE</div>
<div class="abs slide-arrow" style="left:64px;top:311px">&#8249;</div>
<div class="abs slide-arrow" style="left:1098px;top:311px">&#8250;</div>
<div class="abs dots"><span></span><span></span><span class="on"></span><span></span><span></span></div>

<!-- unique -->
<h2 class="abs sec-title script center" style="top:705px">Why we are Unique and Different?</h2>
<p class="abs lead center" style="top:784px">Why have a generic, industrial hand sanitizer when you could have<br>something truly unique and different?</p>

<div class="abs products-photo" role="img" aria-label="Photo of three sanitizer stands with hexagon, rectangular and round wedding photos"></div>

<svg width="0" height="0" style="position:absolute">
  <defs>
    <symbol id="dropIcon" viewBox="0 0 46 56">
      <path d="M23 2C23 2 4 26 4 37a19 19 0 0 0 38 0C42 26 23 2 23 2Z" fill="currentColor"/>
      <circle cx="23" cy="37" r="8" fill="none" stroke="#fff" stroke-width="2.5"/>
    </symbol>
  </defs>
</svg>

<div class="abs feature" style="left:210px;top:1358px"><svg class="drop" style="color:var(--blue)"><use href="#dropIcon"/></svg>CHOOSE A PHOTO</div>
<div class="abs feature" style="left:501px;top:1358px"><svg class="drop" style="color:var(--blue)"><use href="#dropIcon"/></svg>CHOOSE A SIZE</div>
<div class="abs feature" style="left:772px;top:1358px"><svg class="drop" style="color:var(--blue)"><use href="#dropIcon"/></svg>CHOOSE A SHAPE</div>

<div class="abs btn pill" style="left:458px;top:1456px;width:286px;height:49px">CHECK PRICE AND RENT NOW</div>

<!-- customize band -->
<svg class="abs band-bg" width="1200" height="650" viewBox="0 1570 1200 650">
  <defs>
    <linearGradient id="band" x1="0" y1="0" x2="1" y2="0">
      <stop offset="0" stop-color="#0c78c9"/>
      <stop offset="1" stop-color="#2bb0d6"/>
    </linearGradient>
  </defs>
  <path d="M0 1704Q600 1470 1200 1704V2094Q600 2320 0 2094Z" fill="url(#band)"/>
</svg>
<div class="abs frame-line"></div>
<div class="abs" style="left:112px;top:1790px;width:4px;height:252px;background:var(--white)"></div>
<div class="abs" style="left:112px;top:2038px;width:40px;height:4px;background:var(--white)"></div>
<div class="abs band-photo" role="img" aria-label="Sanitizer stand with wedding photo at a candlelit reception hall"></div>
<h2 class="abs band-title script">Customize Your Sanitizer</h2>
<div class="abs band-sub">With Any Photo, Any Size, Any Shape</div>
<div class="abs band-item" style="top:1826px"><svg class="drop" style="color:var(--white);width:40px;height:50px"><use href="#dropIcon"/></svg><span>Customize the photo above the spout and the spout decoration</span></div>
<div class="abs band-item" style="top:1918px"><svg class="drop" style="color:var(--white);width:40px;height:50px"><use href="#dropIcon"/></svg><span>Choose any size and shape photo you wish</span></div>
<div class="abs band-item" style="top:1990px"><svg class="drop" style="color:var(--white);width:40px;height:50px"><use href="#dropIcon"/></svg><span>Choose from our standard spout decorations or design one of your own.&nbsp; We'll take care of producing and fitting it.</span></div>
<div class="abs btn pill" style="left:458px;top:2176px;width:286px;height:48px">CHECK PRICE AND AVAILABILITY</div>

<!-- greet -->
<h2 class="abs greet-title script">Greet Your Guests With An<br>Act Of Care</h2>
<div class="abs care-item" style="top:2436px"><svg class="drop" style="color:var(--blue);width:42px;height:52px"><use href="#dropIcon"/></svg><span>Make your friends and family feel welcome and safe with a rugged, durable hand sanitizer from Purvant</span></div>
<div class="abs care-item" style="top:2523px"><svg class="drop" style="color:var(--blue);width:42px;height:52px"><use href="#dropIcon"/></svg><span>Our battery-powered dispensers are reliable, wireless, and touchless</span></div>
<div class="abs care-item" style="top:2608px"><svg class="drop" style="color:var(--blue);width:42px;height:52px"><use href="#dropIcon"/></svg><span>Filled with your choice from our wide range of sanitizing products</span></div>
<div class="abs btn pill" style="left:153px;top:2700px;width:287px;height:51px">CHECK PRICE AND RENT NOW</div>
<div class="abs greet-photo" role="img" aria-label="Photo of a sanitizer stand with a bride and groom beside a wedding cake"></div>

<!-- review -->
<div class="abs review-bg" role="img" aria-label="Couple dancing under string lights"></div>
<div class="abs review-photo placeholder" role="img" aria-label="Photo of a sanitizer stand with a floral wedding portrait"></div>
<div class="abs review-kicker">Our Hand Sanitizer</div>
<h2 class="abs review-title script">Our Happy Customer<br>Review</h2>
<div class="abs round-arrow" style="left:971px;top:3023px">&#8592;</div>
<div class="abs round-arrow" style="left:1017px;top:3023px">&#8594;</div>
<div class="abs review-card"></div>
<p class="abs quote">Aliquam tincidunt sapien et nisi felacinia ante andeiyfringilla. Nullam vestibulum venenatis ante etporttiteoy into onusce sit ametbib enduerat. Cras vestibulu venenatis ante etporttieoy into onusce sit ametbib enduerat. Cras commodo niduitings felacinia ante andeiyfringilla. Nullam vestibulum venenatis ante etporttiteoy into onusce.</p>
<div class="abs avatar" style="left:638px;top:3340px;width:56px;height:56px" role="img" aria-label="Reviewer portrait"></div>
<div class="abs reviewer">Mara Ellison</div>
<div class="abs reviewer-role">CEO, Bright Loom Studio</div>

<!-- offers -->
<div class="abs offer-kicker">Our Hand Sanitizer</div>
<h2 class="abs offers-title script">Our Special Offers</h2>
<div class="abs offer-card"></div>

<div class="abs avatar" style="left:163px;top:3667px;width:100px;height:100px" role="img" aria-label="Marriage package photo"></div>
<div class="abs offer-price" style="top:3666px">Start From: <b>$ 25.00</b></div>
<div class="abs offer-name" style="top:3688px">Marriage Package</div>
<div class="abs offer-desc" style="top:3726px">Lorem ipsum dolor sit amet, consectetur adipiscing sed do eiusmod tempor</div>

<div class="abs avatar" style="left:163px;top:3818px;width:100px;height:100px" role="img" aria-label="Flower vase package photo"></div>
<div class="abs offer-price" style="top:3816px">Start From: <b>$ 35.00</b></div>
<div class="abs offer-name" style="top:3838px">Flower Vase Package</div>
<div class="abs offer-desc" style="top:3876px">Lorem ipsum dolor sit amet, consectetur adipiscing sed do eiusmod tempor</div>

<div class="abs avatar" style="left:163px;top:3969px;width:100px;height:100px" role="img" aria-label="Wedding cake package photo"></div>
<div class="abs offer-price" style="top:3967px">Start From: <b>$ 50.0</b></div>
<div class="abs offer-name" style="top:3989px">Wedding Cake Package</div>
<div class="abs offer-desc" style="top:4027px">Lorem ipsum dolor sit amet, consectetur adipiscing sed do eiusmod tempor</div>

<div class="abs collage" style="left:650px;top:3591px;width:325px;height:385px;background:linear-gradient(160deg,#e9e4ea,#d6c2b8 50%,#f2f0ee)" role="img" aria-label="Photo of floral vase arrangements at a wedding venue"></div>
<div class="abs collage" style="left:870px;top:3515px;width:213px;height:209px;background:linear-gradient(180deg,#1d1f27,#5a5a5e 60%,#a09b96)" role="img" aria-label="Photo of a couple walking among sparklers at night"></div>
<div class="abs collage" style="left:790px;top:3866px;width:293px;height:231px;background:linear-gradient(150deg,#cfd3d8,#e8d8cf 50%,#f5f5f5)" role="img" aria-label="Photo of hands being washed under a running tap"></div>

<!-- footer -->
<svg class="abs footer-bg" width="1200" height="410" viewBox="0 4160 1200 410">
  <defs>
    <linearGradient id="footSwoosh" x1="0" y1="0" x2="1" y2="0">
      <stop offset="0" stop-color="#0a5fb8"/>
      <stop offset="1" stop-color="#2bb0d6"/>
    </linearGradient>
  </defs>
  <path d="M150 4250Q600 4110 1050 4250Q600 4150 150 4250Z" fill="url(#footSwoosh)"/>
  <path d="M0 4240Q600 4140 1200 4240V4570H0Z" fill="#131a2a"/>
</svg>
<div class="abs footer-brand">purvant</div>

<div class="abs foot-head" style="left:160px">CONTACT US</div>
<div class="abs foot-line" style="top:4389px">
  <svg width="14" height="14" viewBox="0 0 24 24"><path d="M6.6 10.8a15 15 0 0 0 6.6 6.6l2.2-2.2a1 1 0 0 1 1-.25 11.4 11.4 0 0 0 3.6.57 1 1 0 0 1 1 1V20a1 1 0 0 1-1 1A17 17 0 0 1 3 4a1 1 0 0 1 1-1h3.5a1 1 0 0 1 1 1c0 1.25.2 2.45.57 3.57a1 1 0 0 1-.25 1Z" fill="#fff"/></svg>
  (+1) 555 204 3318
</div>
<div class="abs foot-line" style="top:4434px">
  <svg width="12" height="16" viewBox="0 0 24 32"><path d="M12 0a12 12 0 0 0-12 12c0 9 12 20 12 20s12-11 12-20A12 12 0 0 0 12 0Zm0 16a4 4 0 1 1 0-8 4 4 0 0 1 0 8Z" fill="#fff"/></svg>
  48 Lantern Row, Alder, USA
</div>

<div class="abs foot-head" style="left:481px">FOLLOW US</div>
<div class="abs social" style="left:482px;top:4393px" aria-label="Social profile one"></div>
<div class="abs social" style="left:531px;top:4393px" aria-label="Social profile two"></div>
<div class="abs social" style="left:578px;top:4393px" aria-label="Social profile three"></div>
<div class="abs social" style="left:630px;top:4393px" aria-label="Social profile four"></div>

<div class="abs foot-head" style="left:779px">NEWSLETTER SUBSCRIBE</div>
<div class="abs email">Enter Email</div>
<svg class="abs" style="left:1012px;top:4404px" width="14" height="11" viewBox="0 0 14 11"><rect width="14" height="11" rx="1" fill="#333"/><path d="M0 1l7 5 7-5" stroke="#fff" stroke-width="1.3" fill="none"/></svg>
<div class="abs btn subscribe">SUBSCRIBE</div>

<div class="abs rule"></div>
<div class="abs copy">Copyrights © 2021 Purvant.&nbsp; All Rights Reserved &nbsp; | &nbsp; Site Map &nbsp; | &nbsp; Privacy Policy.</div>

</body>
</html>
```